Editorial Website Design for High-End Custom Millwork Firm

Design (no development) for a 5-7 page website for a high-end custom architectural millwork firm. Editorial, magazine-quality aesthetic — think Dwelling Quarterly and top-tier millwork studios (Owen Tallard, Vorko). Full brief, reference sites, and project photography attached. We have uploaded a sample of our photography to use in your design. PLEASE READ PDF DOCUMENT BRIEF!!!

```html
<!DOCTYPE html>
<html lang="en">
<head>
<meta charset="utf-8">
<title>Halden Residential — Custom Architectural Millwork</title>
<link href="https://fonts.googleapis.com/css2?family=Cormorant+Garamond:wght@500;600&family=Poppins:wght@300;400;500&display=swap" rel="stylesheet">
<style>
:root{
  --cream:#efe9e2;
  --ink:#1c1414;
  --maroon:#1f0505;
  --red:#a3141b;
  --tan:#8b6a53;
  --muted:#5c5350;
  --white:#ffffff;
  --line:#d9d1c8;
  --serif:"Cormorant Garamond", Georgia, serif;
  --sans:"Poppins", Arial, sans-serif;
}
*{box-sizing:border-box;margin:0;padding:0}
html,body{width:1200px;height:4777px;overflow:hidden;background:var(--cream)}
body{font-family:var(--sans);color:var(--ink)}
.page{position:relative;width:1200px;height:4777px;overflow:hidden}
.abs{position:absolute}
.photo{position:absolute;border-radius:6px}
.serif{font-family:var(--serif);font-weight:500;line-height:.95;letter-spacing:-.5px}

/* buttons */
.btn{position:absolute;display:flex;align-items:center;gap:12px;height:38px;padding:0 6px 0 14px;font-size:12px;border-radius:2px;white-space:nowrap}
.btn-red{background:var(--red);color:var(--white)}
.btn-ghost{border:1.5px solid var(--white);color:var(--white);background:rgba(0,0,0,.2)}
.btn-outline{border:1.5px solid #8a8380;color:var(--ink)}
.btn .ico{width:26px;height:26px;display:flex;align-items:center;justify-content:center;background:var(--white);border-radius:2px}
.btn-outline .ico{background:transparent}
.arrow-box{position:absolute;width:30px;height:30px;background:var(--white);border-radius:2px;display:flex;align-items:center;justify-content:center}

/* hero */
.hero{left:0;top:0;width:1200px;height:733px;background:radial-gradient(ellipse at 50% 35%,#6b4a35 0%,#3a261b 45%,#1c120c 100%)}
.hero::after{content:"";position:absolute;inset:0;background:linear-gradient(180deg,rgba(0,0,0,.35),rgba(0,0,0,.15) 40%,rgba(0,0,0,.45))}
.brand{left:113px;top:36px;display:flex;align-items:center;gap:10px;z-index:2;color:var(--white);font-family:var(--serif);font-weight:500;font-size:24px;white-space:nowrap}
.brand .sq{width:14px;height:14px;background:var(--tan)}
.nav{left:354px;top:40px;display:flex;gap:20px;font-size:15px;color:#e9e2dc;z-index:2}
.nav .active{color:var(--white);font-weight:500}
.phone{left:920px;top:30px;width:167px;height:40px;background:var(--tan);color:var(--white);font-size:15px;display:flex;align-items:center;justify-content:space-between;padding:0 5px 0 14px;border-radius:2px;z-index:2}
.phone .ico{width:30px;height:30px;background:var(--white);border-radius:2px;display:flex;align-items:center;justify-content:center}
.hero-title{z-index:2;color:var(--white);font-family:var(--serif);font-weight:500;font-size:92px;line-height:1;white-space:nowrap}
.hero-title small{font-size:52px}
.hero-sub{z-index:2;left:330px;top:384px;width:214px;text-align:right;color:#eee;font-size:17px;line-height:26px}

/* about */
.about h2{left:451px;top:812px;font-size:60px;color:var(--ink)}
.about p{position:absolute;font-size:12.5px;line-height:18px;color:var(--muted)}

/* services */
.services{left:11px;top:1304px;width:1178px;height:705px;background:var(--maroon);border-radius:16px}
.svc-label{position:absolute;color:var(--white);font-size:17px;font-weight:500}

/* vision */
.vision h2{left:0;top:2076px;width:1200px;text-align:center;font-size:64px;line-height:.92}
.vision .lead{left:370px;top:2208px;width:460px;text-align:center;font-size:13px;line-height:20px;color:var(--muted)}
.step{position:absolute;top:2302px;width:234px;height:195px;background:var(--white);border-radius:3px;padding:0 16px}
.step .badge{margin-top:14px;width:40px;height:40px;background:#f6e3e3;border-radius:3px;display:flex;align-items:center;justify-content:center}
.step h3{font-family:var(--serif);font-weight:500;font-size:22px;margin-top:26px}
.step p{font-size:11.5px;line-height:17px;color:var(--muted);margin-top:14px}

/* why */
.why h2{left:115px;top:2584px;font-size:64px}
.why .lead{left:597px;top:2580px;width:470px;font-size:13px;line-height:21.5px;color:var(--muted)}
.acc-open{left:638px;top:2755px;width:445px;height:111px;background:var(--white);border-radius:3px;padding:16px 18px}
.acc-open .q{display:flex;justify-content:space-between;font-size:14.5px}
.acc-open .a{margin-top:16px;padding-top:14px;border-top:1px solid var(--line);font-size:12px;line-height:19px;color:var(--muted)}
.acc{position:absolute;left:654px;width:393px;display:flex;justify-content:space-between;font-size:14.5px;color:#3c3432;padding-bottom:16px;border-bottom:1px solid var(--line)}

/* projects */
.projects{left:11px;top:3259px;width:1178px;height:705px;background:var(--maroon);border-radius:16px}
.slide-label{left:336px;top:3812px;color:var(--white);font-size:17px;font-weight:500}
.progress{left:119px;top:3900px;width:250px;height:3px;background:var(--white)}
.progress span{display:block;width:154px;height:3px;background:var(--red)}
.circ{position:absolute;top:3882px;width:38px;height:38px;border-radius:50%;background:var(--white);display:flex;align-items:center;justify-content:center}

/* cta */
.cta h2{left:0;top:4050px;width:1200px;text-align:center;font-size:52px;line-height:.93}
.cta .lead{left:420px;top:4220px;width:360px;text-align:center;font-size:13px;line-height:20px;color:var(--muted)}

/* footer */
.footer{left:0;top:4476px;width:1200px;height:301px;background:var(--maroon);color:#e6dcd6}
.footer h4{position:absolute;font-size:12px;font-weight:500;color:var(--white)}
.footer .col{position:absolute;font-size:12.5px;line-height:19.5px;color:#b7a9a3}
.footer .contact{position:absolute;left:154px;font-size:12.5px;line-height:19.5px;color:#d8ccc6;display:flex;gap:8px}
.newsletter{position:absolute;left:810px;top:166px;width:242px;height:32px;display:flex;border-radius:16px;overflow:hidden}
.newsletter .field{flex:1;background:var(--white);color:#8c8380;font-size:11px;line-height:32px;padding-left:20px}
.newsletter .go{width:102px;background:var(--red);color:var(--white);font-size:12px;font-weight:500;line-height:32px;text-align:center}
.footer .rule{position:absolute;left:0;top:230px;width:1200px;height:1px;background:#4a3030}
.footer .copy{position:absolute;left:152px;top:257px;font-size:12.5px;color:#cfc3bd}
.social{position:absolute;top:258px;display:flex;gap:14px;left:970px}
.social span{width:12px;height:12px;border-radius:50%;background:var(--white)}
</style>
</head>
<body>
<div class="page">

  <!-- Hero -->
  <section class="hero abs" role="img" aria-label="Photo of a dark wood-panelled retail interior with pendant lights and lattice panels"></section>
  <div class="brand abs"><span class="sq"></span>Halden Residential</div>
  <nav class="nav abs"><span class="active">Home</span><span>About</span><span>Portfolio</span><span>Case Study</span><span>Services</span><span>Blog</span><span>Contact</span></nav>
  <div class="phone abs">555-014-2290<span class="ico"><svg width="16" height="16" viewBox="0 0 24 24" fill="none" stroke="#8b6a53" stroke-width="2"><path d="M5 3h4l2 5-3 2a12 12 0 0 0 6 6l2-3 5 2v4a2 2 0 0 1-2 2A17 17 0 0 1 3 5a2 2 0 0 1 2-2z"/></svg></span></div>
  <div class="hero-title abs" style="left:441px;top:206px"><small>We</small> DESIGN</div>
  <div class="hero-title abs" style="left:462px;top:286px">SPACES <small>that</small></div>
  <div class="hero-title abs" style="left:551px;top:366px">WORK.</div>
  <div class="hero-sub abs">Custom Architectural Millwork &amp; Cabinetry</div>
  <div class="btn btn-red" style="left:447px;top:484px;z-index:2">Start Your Project<span class="ico"><svg width="12" height="12" viewBox="0 0 12 12" fill="none" stroke="#a3141b" stroke-width="1.6"><path d="M1 6h10M7 2l4 4-4 4"/></svg></span></div>
  <div class="btn btn-ghost" style="left:616px;top:484px;z-index:2">View Our Wok<span class="ico"><svg width="12" height="12" viewBox="0 0 12 12" fill="none" stroke="#1c1414" stroke-width="1.6"><path d="M1 6h10M7 2l4 4-4 4"/></svg></span></div>

  <!-- About -->
  <section class="about">
    <div class="photo" style="left:111px;top:814px;width:316px;height:408px;background:linear-gradient(160deg,#9fb4c4,#e9e4dc 45%,#6a4a36)" role="img" aria-label="Photo of a white arched built-in cabinet with shelves of plates and a vase of flowers"></div>
    <div class="photo" style="left:781px;top:814px;width:304px;height:219px;background:linear-gradient(160deg,#b9ccd8,#eef0ee 50%,#3b4656)" role="img" aria-label="Photo of a bright kitchen with white cabinetry and a pendant lantern"></div>
    <h2 class="abs serif">PLAN.<br>DESIGN.<br>BUILD.</h2>
    <p style="left:453px;top:998px;width:290px">Halden Millwork is an award-quality custom architectural millwork and cabinetry firm based in Ashford, North Carolina</p>
    <p style="left:453px;top:1070px;width:620px">We produce high-end commercial interiors (hotels, universities, luxury retail) and residential built-ins for architects, interior designers, and discerning homeowners.</p>
    <p style="left:453px;top:1121px;width:620px">We hold the Keystone Craft Standard at Premium Grade — the highest tier in the industry —. Roughly 70% of our work is commercial and 30% residential.</p>
    <div class="btn btn-red" style="left:451px;top:1184px">About Us<span class="ico"><svg width="12" height="12" viewBox="0 0 12 12" fill="none" stroke="#a3141b" stroke-width="1.6"><path d="M1 6h10M7 2l4 4-4 4"/></svg></span></div>
  </section>

  <!-- Services -->
  <section class="services abs"></section>
  <h2 class="abs serif" style="left:111px;top:1388px;font-size:64px;color:#fff">OUR<br>SERVICES.</h2>
  <div class="photo" style="left:113px;top:1558px;width:314px;height:353px;background:linear-gradient(180deg,#6b4a2e,#8e3a22 60%,#3a2418)" role="img" aria-label="Photo of a lounge with red sofas and green walls"></div>
  <div class="photo" style="left:443px;top:1397px;width:316px;height:248px;background:linear-gradient(180deg,#7a6656,#4a4058 60%,#2b2430)" role="img" aria-label="Photo of a commercial bar interior with coffered wood ceiling"></div>
  <div class="photo" style="left:443px;top:1662px;width:316px;height:249px;background:linear-gradient(180deg,#6c5a48,#3f3a36 60%,#2a2420)" role="img" aria-label="Photo of a hotel lobby staircase with wood railings"></div>
  <div class="photo" style="left:772px;top:1397px;width:313px;height:516px;background:linear-gradient(180deg,#e8e2da,#b77a46 55%,#2e2a28)" role="img" aria-label="Photo of a kitchen with wood cabinetry and a dark island"></div>
  <span class="svc-label" style="left:460px;top:1612px">Commercial Interiors</span>
  <span class="svc-label" style="left:130px;top:1878px">Residential Interiors</span>
  <span class="svc-label" style="left:460px;top:1878px">Interior Designers</span>
  <span class="svc-label" style="left:789px;top:1879px">Interior Designers</span>
  <div class="arrow-box" style="left:715px;top:1606px"><svg width="13" height="13" viewBox="0 0 12 12" fill="none" stroke="#a3141b" stroke-width="1.6"><path d="M1 6h10M7 2l4 4-4 4"/></svg></div>
  <div class="arrow-box" style="left:384px;top:1872px"><svg width="13" height="13" viewBox="0 0 12 12" fill="none" stroke="#a3141b" stroke-width="1.6"><path d="M1 6h10M7 2l4 4-4 4"/></svg></div>
  <div class="arrow-box" style="left:715px;top:1872px"><svg width="13" height="13" viewBox="0 0 12 12" fill="none" stroke="#a3141b" stroke-width="1.6"><path d="M1 6h10M7 2l4 4-4 4"/></svg></div>
  <div class="arrow-box" style="left:1043px;top:1874px"><svg width="13" height="13" viewBox="0 0 12 12" fill="none" stroke="#a3141b" stroke-width="1.6"><path d="M1 6h10M7 2l4 4-4 4"/></svg></div>

  <!-- Vision -->
  <section class="vision">
    <h2 class="abs serif">FROM VISION TO<br>REALITY.</h2>
    <p class="abs lead">Every successful space begins with clarity and ends with precision. Our structured approach ensures creativity is supported bystrategy, Planning and flawless execution.</p>
    <div class="step" style="left:113px"><div class="badge"><svg width="22" height="22" viewBox="0 0 24 24" fill="none" stroke="#a3141b" stroke-width="2"><path d="M2 12s4-7 10-7 10 7 10 7-4 7-10 7S2 12 2 12z"/><circle cx="12" cy="12" r="3"/></svg></div><h3>Discover</h3><p>We understand your business and define a clear strategic direction for the space</p></div>
    <div class="step" style="left:360px"><div class="badge"><svg width="22" height="22" viewBox="0 0 24 24" fill="none" stroke="#a3141b" stroke-width="2"><rect x="5" y="3" width="14" height="18" rx="1"/><path d="M8 8h8M8 12h8M8 16h5"/></svg></div><h3>Plan</h3><p>We understand your business and define a clear strategic direction for the space</p></div>
    <div class="step" style="left:607px"><div class="badge"><svg width="22" height="22" viewBox="0 0 24 24" fill="none" stroke="#a3141b" stroke-width="2"><rect x="3" y="5" width="18" height="14" rx="1"/><path d="M7 15l8-8 2 2-8 8H7z"/></svg></div><h3>Design</h3><p>We understand your business and define a clear strategic direction for the space</p></div>
    <div class="step" style="left:853px"><div class="badge"><svg width="22" height="22" viewBox="0 0 24 24" fill="none" stroke="#a3141b" stroke-width="2"><path d="M3 10l5-4 4 3 4-3 5 4-9 9z"/></svg></div><h3>Build</h3><p>We understand your business and define a clear strategic direction for the space</p></div>
  </section>

  <!-- Why -->
  <section class="why">
    <h2 class="abs serif">WHY WORK<br>WITH US?.</h2>
    <p class="abs lead">We design offices that inc our strength lies in bridging design and execution - ensuring bold ideas are delivered with reliability, efficiency, and attention to detail.rease productivity, retail spaces that elevate customer experience, and hospitality interiors that create lasting impressions.</p>
    <div class="photo" style="left:111px;top:2753px;width:486px;height:417px;background:linear-gradient(150deg,#8a8a86,#d8d4cc 50%,#5a5a52)" role="img" aria-label="Photo of a craftsman assembling a white lattice panel in a workshop"></div>
    <div class="acc-open abs"><div class="q">Integrated design &amp; shopfitting expertise<svg width="12" height="12" viewBox="0 0 12 12" fill="none" stroke="#555" stroke-width="1.4"><path d="M2 4l4 4 4-4"/></svg></div><div class="a">Lorem Ipsum is simply dummy text of the printing and typesetting industry. Lorem Ipsum has been the industry's.</div></div>
    <div class="acc" style="top:2890px">Quality project delivery<svg width="12" height="12" viewBox="0 0 12 12" fill="none" stroke="#555" stroke-width="1.4"><path d="M2 4l4 4 4-4"/></svg></div>
    <div class="acc" style="top:2947px">Structured project management<svg width="12" height="12" viewBox="0 0 12 12" fill="none" stroke="#555" stroke-width="1.4"><path d="M2 4l4 4 4-4"/></svg></div>
    <div class="acc" style="top:3010px">Clear budgeting and timelines<svg width="12" height="12" viewBox="0 0 12 12" fill="none" stroke="#555" stroke-width="1.4"><path d="M2 4l4 4 4-4"/></svg></div>
    <div class="acc" style="top:3069px">Tailored,, client-focused solutions<svg width="12" height="12" viewBox="0 0 12 12" fill="none" stroke="#555" stroke-width="1.4"><path d="M2 4l4 4 4-4"/></svg></div>
    <div class="btn btn-red" style="left:658px;top:3131px">About Us<span class="ico"><svg width="12" height="12" viewBox="0 0 12 12" fill="none" stroke="#a3141b" stroke-width="1.6"><path d="M1 6h10M7 2l4 4-4 4"/></svg></span></div>
  </section>

  <!-- Projects -->
  <section class="projects abs"></section>
  <h2 class="abs serif" style="left:111px;top:3316px;font-size:64px;color:#fff">OUR<br>PROJECTS.</h2>
  <p class="abs" style="left:627px;top:3310px;width:450px;font-size:13px;line-height:21.5px;color:#e5dcd8">We design offices that incOur strength lies in bridging design and execution - ensuring bold ideas are delivered with reliability, efficiency, and attention to detail.rease productivity.</p>
  <div class="btn btn-red" style="left:627px;top:3394px">View All Projects<span class="ico"><svg width="12" height="12" viewBox="0 0 12 12" fill="none" stroke="#a3141b" stroke-width="1.6"><path d="M1 6h10M7 2l4 4-4 4"/></svg></span></div>
  <div class="photo" style="left:117px;top:3491px;width:81px;height:362px;border-radius:12px;background:linear-gradient(180deg,#d8d6d0,#9b7a5a)" role="img" aria-label="Photo of white shelving with dishware"></div>
  <div class="photo" style="left:213px;top:3491px;width:82px;height:362px;border-radius:12px;background:linear-gradient(180deg,#8a6a4e,#3e3640)" role="img" aria-label="Photo of wood slat wall with bar stools"></div>
  <div class="photo" style="left:310px;top:3491px;width:584px;height:362px;border-radius:12px;background:linear-gradient(170deg,#6e5a4a,#a05a2e 45%,#3a3048 70%,#1f1a18)" role="img" aria-label="Photo of a boutique lounge with a purple sofa and carved wood screen"></div>
  <div class="photo" style="left:907px;top:3491px;width:82px;height:362px;border-radius:12px;background:linear-gradient(180deg,#b69a78,#6e4a2e)" role="img" aria-label="Photo of a retail clothing alcove"></div>
  <div class="photo" style="left:1002px;top:3491px;width:83px;height:362px;border-radius:12px;background:linear-gradient(180deg,#cbbba8,#8a5a32)" role="img" aria-label="Photo of wood cabinetry with wine storage"></div>
  <span class="abs slide-label">Marlow &amp; Finch – NYC</span>
  <div class="arrow-box" style="left:842px;top:3806px"><svg width="13" height="13" viewBox="0 0 12 12" fill="none" stroke="#a3141b" stroke-width="1.6"><path d="M1 6h10M7 2l4 4-4 4"/></svg></div>
  <div class="abs progress"><span></span></div>
  <div class="circ" style="left:998px"><svg width="14" height="14" viewBox="0 0 12 12" fill="none" stroke="#a3141b" stroke-width="1.6"><path d="M11 6H1M5 2L1 6l4 4"/></svg></div>
  <div class="circ" style="left:1048px"><svg width="14" height="14" viewBox="0 0 12 12" fill="none" stroke="#a3141b" stroke-width="1.6"><path d="M1 6h10M7 2l4 4-4 4"/></svg></div>

  <!-- CTA -->
  <section class="cta">
    <div class="photo" style="left:113px;top:4031px;width:197px;height:165px;background:linear-gradient(160deg,#d8d8d2,#9aa89a)" role="img" aria-label="Photo of a white kitchen"></div>
    <div class="photo" style="left:130px;top:4185px;width:256px;height:211px;background:linear-gradient(160deg,#8a5a36,#c79a6a 50%,#4a3a30)" role="img" aria-label="Photo of a lounge with carved wood screens"></div>
    <div class="photo" style="left:889px;top:4031px;width:196px;height:230px;background:linear-gradient(160deg,#8aa2b8,#dfe2e0)" role="img" aria-label="Photo of a blue-grey panelled room"></div>
    <div class="photo" style="left:842px;top:4176px;width:193px;height:230px;background:linear-gradient(180deg,#6a4e3a,#c8a880 50%,#2a2020)" role="img" aria-label="Photo of a boutique display with shelving"></div>
    <h2 class="abs serif">READY TO<br>TRANSFORM YOUR<br>SPACE?</h2>
    <p class="abs lead">Let's crate and environment that reflects your brand and drives your business forward</p>
    <div class="btn btn-red" style="left:452px;top:4302px">Start Your Project<span class="ico"><svg width="12" height="12" viewBox="0 0 12 12" fill="none" stroke="#a3141b" stroke-width="1.6"><path d="M1 6h10M7 2l4 4-4 4"/></svg></span></div>
    <div class="btn btn-outline" style="left:620px;top:4302px">View Our Wok<span class="ico"><svg width="12" height="12" viewBox="0 0 12 12" fill="none" stroke="#1c1414" stroke-width="1.6"><path d="M1 6h10M7 2l4 4-4 4"/></svg></span></div>
  </section>

  <!-- Footer -->
  <footer class="footer abs">
    <h4 style="left:154px;top:48px">Contact Us</h4>
    <div class="contact" style="top:80px"><svg width="12" height="14" viewBox="0 0 12 14" fill="none" stroke="#d8ccc6" stroke-width="1.3"><path d="M6 13s5-4.5 5-8A5 5 0 0 0 1 5c0 3.5 5 8 5 8z"/><circle cx="6" cy="5" r="1.8"/></svg><span>Halden Architectural Millwork<br>118 Larkspur Lane<br>Ashford, NC 27000</span></div>
    <div class="contact" style="top:152px"><svg width="13" height="13" viewBox="0 0 24 24" fill="none" stroke="#d8ccc6" stroke-width="2"><path d="M5 3h4l2 5-3 2a12 12 0 0 0 6 6l2-3 5 2v4a2 2 0 0 1-2 2A17 17 0 0 1 3 5a2 2 0 0 1 2-2z"/></svg><span>555.014.7731</span></div>
    <div class="contact" style="top:184px"><svg width="13" height="11" viewBox="0 0 13 11" fill="none" stroke="#d8ccc6" stroke-width="1.3"><rect x="1" y="1" width="11" height="9"/><path d="M1 1l5.5 5L12 1"/></svg><span>hello@haldenmillwork.com</span></div>
    <h4 style="left:428px;top:68px">QUICK LINKS</h4>
    <div class="col" style="left:428px;top:90px">Home<br>About<br>Portfolio<br>Case Study</div>
    <h4 style="left:618px;top:68px">QUICK LINKS</h4>
    <div class="col" style="left:618px;top:90px">Services<br>Blog<br>Contact Us<br>Tearms</div>
    <h4 style="left:811px;top:68px">WRITE TO US</h4>
    <div class="col" style="left:811px;top:90px;width:210px">Provide your email below to subscribe to our newsletter</div>
    <div class="newsletter"><span class="field">Email address</span><span class="go">Subscribe</span></div>
    <div class="rule"></div>
    <div class="copy">Copyright 2026 haldenmillwork.com. All Rights Reserved.</div>
    <div class="social" aria-label="Social links"><span></span><span></span><span></span></div>
  </footer>

</div>
</body>
</html>
```